New Packaging Design Project LONDON INSPIRED BEAUTY PACKAGING

WE MUST RECEIVE THE FINAL IMAGE IN A FILE READY TO BE SENT TO THE HOT STAMPER AND PRINTER

we need a London Inspired look (images attached can be used)
Vector files are attaches and need to be used for the front images

SIZE
the palette is square and 4.5 X 4.5 inches

This is a beauty palette for the face inspired by London

We want HQ artwork that will be elegant, feminine and fun. This is a high end brand and we need good quality artwork that will capture our audience from ages 20-3

on the top of the palette we need our logo (INCLUDED IN IMAGES ) (MARLOW 82)

The background must not be black or blank because it will just blend into the palette paper which is black. We want this artwork to stand out!

BACK OF THE PALETTE

Our logo needs to also be on the back

Under the logo we need to have 4 circles with the shade names in the circles

lower half of the back of the palette:

We need Vegan, Cruelty free and makeup artist approved stamp or sign on the back
in rose gold ( we will submit the images once front is completed)
The font: https://www.typefernery.net/quillan-hand.font?psize=l&text=Amber+Dusk+Palette

Id like to see the corvane colors incorporated either (Most likely in the font)

(NO UNION JACK ON THE ARTWORK)

Target Market(s)

18-30

Industry/Entity Type

Printer

Requirements
Should not have
• (NO UNION JACK ON THE ARTWORK)

```html
<!DOCTYPE html>
<html lang="en">
<head>
<meta charset="utf-8">
<title>Marlow 82 – The Amber Dusk Palette packaging</title>
<link rel="stylesheet" href="https://fonts.googleapis.com/css2?family=Pinyon+Script&family=Raleway:wght@400;500&display=swap">
<style>
  :root {
    --stage-light: #f4f4f4;
    --stage-dark: #d9d9d9;
    --cream: #f3e8d5;
    --cream-shade: #e6dccd;
    --warm-grey: #cfc7bb;
    --gold: #c9a14a;
    --gold-deep: #a8822f;
    --logo-ink: #3f8f86;
    --ink: #2a2220;
    --rose-gold: #d6a49a;
    --bus-red: #d8302f;
    --bus-gold: #c9a14a;
  }
  * { box-sizing: border-box; margin: 0; padding: 0; }
  html, body { width: 1200px; height: 686px; overflow: hidden; }
  body {
    background: radial-gradient(ellipse at center, var(--stage-light) 0%, var(--stage-dark) 100%);
    position: relative;
    font-family: "Raleway", sans-serif;
  }
  .palette {
    position: absolute;
    top: 87px;
    width: 515px;
    height: 515px;
    border: 6px solid var(--gold);
    box-shadow: inset 0 0 0 1px var(--gold-deep);
    overflow: hidden;
  }
  .palette--front { left: 62px; }
  .palette--back { left: 623px; }

  .surface {
    position: absolute;
    inset: 0;
    background:
      radial-gradient(ellipse at 50% 50%, var(--cream) 0%, var(--cream) 45%, var(--cream-shade) 80%, var(--warm-grey) 100%);
  }

  .brand {
    position: absolute;
    left: 0;
    right: 0;
    text-align: center;
  }
  .brand__name {
    display: inline-flex;
    align-items: center;
    gap: 6px;
    font-size: 15px;
    font-weight: 500;
    color: var(--logo-ink);
    letter-spacing: .5px;
  }
  .brand__dot {
    width: 7px;
    height: 7px;
    border-radius: 50%;
    background: var(--logo-ink);
  }
  .brand__by {
    display: block;
    margin-top: 8px;
    font-size: 5px;
    letter-spacing: 1px;
    color: var(--ink);
    text-transform: uppercase;
  }
  .palette--front .brand { top: 34px; }
  .palette--back .brand { top: 68px; }

  .title {
    position: absolute;
    top: 96px;
    left: 20px;
    right: 20px;
    text-align: center;
    font-family: "Pinyon Script", cursive;
    font-size: 42px;
    font-weight: 400;
    line-height: 1;
    color: var(--gold);
    text-shadow: 1px 1px 0 var(--gold-deep);
    white-space: nowrap;
  }

  .artwork {
    position: absolute;
    left: 50px;
    top: 158px;
    width: 412px;
    height: 334px;
    border-radius: 6px;
    background: linear-gradient(160deg, #3b2a27 0%, #8a3a34 28%, var(--bus-red) 55%, #b52a2a 80%, var(--bus-gold) 100%);
    opacity: .9;
  }

  .shades {
    position: absolute;
    left: 52px;
    top: 168px;
    display: grid;
    grid-template-columns: repeat(4, 94px);
    grid-template-rows: repeat(2, 94px);
    column-gap: 11px;
    row-gap: 26px;
  }
  .shade {
    border-radius: 50%;
    display: flex;
    align-items: center;
    justify-content: center;
    font-family: "Pinyon Script", cursive;
    font-size: 24px;
    color: var(--ink);
  }
  .shade--1 { background: radial-gradient(circle at 40% 35%, #e9bd95, #d29c72); }
  .shade--2 { background: radial-gradient(circle at 40% 35%, #e39a96, #c5706f); }
  .shade--3 { background: radial-gradient(circle at 40% 35%, #c7a3a6, #a98286); }
  .shade--4 { background: radial-gradient(circle at 40% 35%, #c36e9d, #9c4176); }
  .shade--5 { background: radial-gradient(circle at 40% 35%, #eeb24a, #d48b22); }
  .shade--6 { background: radial-gradient(circle at 40% 35%, #7f605e, #5b4040); }
  .shade--7 { background: radial-gradient(circle at 40% 35%, #e8bf92, #cf9e6e); }
  .shade--8 { background: radial-gradient(circle at 40% 35%, #cb4f62, #a72f45); }

  .seals {
    position: absolute;
    left: 306px;
    top: 428px;
    display: flex;
    align-items: center;
    gap: 14px;
  }
  .seal { background: var(--rose-gold); opacity: .85; }
  .seal--cruelty-free { width: 34px; height: 34px; border-radius: 50%; }
  .seal--vegan { width: 30px; height: 30px; }
  .seal--artist-approved { width: 56px; height: 40px; border-radius: 4px; opacity: .6; }
</style>
</head>
<body>

  <section class="palette palette--front" aria-label="Palette lid">
    <div class="surface" role="img" aria-label="Woven check pattern in cream, warm grey and coral"></div>

    <div class="brand">
      <span class="brand__name"><span class="brand__dot"></span>Marlow 82</span>
      <span class="brand__by">by Elodie Hart</span>
    </div>

    <h1 class="title">The Amber Dusk Palette</h1>

    <div class="artwork" role="img" aria-label="Illustration of two fashionable women taking tea on top of a red double-decker bus with gold glitter accents"></div>
  </section>

  <section class="palette palette--back" aria-label="Palette base">
    <div class="surface" role="img" aria-label="Woven check pattern in cream, warm grey and coral"></div>

    <div class="brand">
      <span class="brand__name"><span class="brand__dot"></span>Marlow 82</span>
      <span class="brand__by">by Elodie Hart</span>
    </div>

    <div class="shades">
      <div class="shade shade--1">Shade 1</div>
      <div class="shade shade--2">Shade 2</div>
      <div class="shade shade--3">Shade 3</div>
      <div class="shade shade--4">Shade 4</div>
      <div class="shade shade--5">Shade 5</div>
      <div class="shade shade--6">Shade 6</div>
      <div class="shade shade--7">Shade 7</div>
      <div class="shade shade--8">Shade 8</div>
    </div>

    <div class="seals">
      <div class="seal seal--cruelty-free" role="img" aria-label="Cruelty free seal"></div>
      <div class="seal seal--vegan" role="img" aria-label="Vegan seal"></div>
      <div class="seal seal--artist-approved" role="img" aria-label="Makeup artist approved seal"></div>
    </div>
  </section>

</body>
</html>
```